Visitenkarten-Design für Erfindung & Entwicklung von Produkten für Körper, Geist und Seele
Zielgruppe
Erfindung und Entwicklung von Produkten für Körper Geist und Seele
Als grosser Überbegriff Produkte zur Regenration und Wohlbefinden sowie Bewusstseins Förderung
' Beispiel ' www. o-senva.ch
Zielgruppe Jedermann und Jedefrau die Ihr Bewusstein für Ihre Gesundheit und Heilung auf allen Ebenen vertiefen möchte ....
Aufgabenstellung
Das Logo ist Entwickelt in einem Entwurfsstadium kleine Verbesserungsvorschläge wären möglich
Vorallem geht es um das Layout und der sauberen Daten Erfassung
sowie die Gestaltung der Visitenkarte

```html
<!DOCTYPE html>
<html lang="de">
<head>
<meta charset="utf-8">
<title>Solvarin – Visitenkarte</title>
<link rel="stylesheet" href="https://fonts.googleapis.com/css2?family=Gudea:wght@400;700&family=Caveat:wght@600&display=swap">
<style>
  :root {
    --bg: #ffffff;
    --frame-green: #6b8e23;
    --edge-rose: #c07a7a;
    --leaf-rose: #d8a9a9;
    --name-red: #7a0a0a;
    --muted-rose: #b07373;
    --tagline-olive: #a8920f;
    --logo-ink: #2b2b2b;
  }
  html, body {
    margin: 0;
    width: 1200px;
    height: 986px;
    overflow: hidden;
    background: var(--bg);
  }
  .canvas {
    position: relative;
    width: 1200px;
    height: 986px;
    font-family: "Gudea", "Trebuchet MS", sans-serif;
  }
  .card-frame {
    position: absolute;
    left: 209px; top: 226px;
    width: 766px; height: 483px;
    border: 4px solid var(--frame-green);
    border-radius: 2px;
  }
  .card-edge {
    position: absolute;
    left: 0; top: 0;
    width: 1200px; height: 986px;
  }
  .foliage {
    position: absolute;
    border-radius: 40% 10% 40% 10%;
    opacity: .45;
  }
  .foliage--top {
    left: 495px; top: 252px;
    width: 468px; height: 176px;
    background: radial-gradient(ellipse at 65% 40%, var(--leaf-rose) 0%, rgba(216,169,169,.35) 55%, rgba(216,169,169,0) 80%);
  }
  .foliage--bottom {
    left: 233px; top: 488px;
    width: 334px; height: 205px;
    background: radial-gradient(ellipse at 40% 55%, var(--leaf-rose) 0%, rgba(216,169,169,.35) 55%, rgba(216,169,169,0) 80%);
  }
  .person-name {
    position: absolute;
    right: 249px; top: 277px;
    margin: 0;
    font-size: 53px;
    font-weight: 700;
    color: var(--name-red);
    letter-spacing: -.5px;
    line-height: 1;
  }
  .contact {
    position: absolute;
    right: 249px; top: 344px;
    margin: 0;
    text-align: right;
    font-size: 17px;
    line-height: 26px;
    color: var(--name-red);
  }
  .brand {
    position: absolute;
    left: 274px; top: 392px;
    display: flex;
    align-items: center;
    gap: 22px;
  }
  .brand__mark {
    width: 26px; height: 26px;
    background: var(--logo-ink);
  }
  .brand__name {
    font-size: 82px;
    font-weight: 400;
    letter-spacing: 22px;
    color: var(--logo-ink);
    line-height: 1;
  }
  .tagline {
    position: absolute;
    left: 612px; top: 536px;
    margin: 0;
    font-family: "Caveat", "Comic Sans MS", cursive;
    font-weight: 600;
    font-size: 50px;
    color: var(--tagline-olive);
    line-height: 1;
  }
  .address {
    position: absolute;
    right: 257px; top: 630px;
    margin: 0;
    text-align: right;
    color: var(--muted-rose);
    line-height: 31px;
  }
  .address__web { font-size: 18px; }
  .address__street { font-size: 20px; }
</style>
</head>
<body>
<main class="canvas">
  <div class="card-frame"></div>

  <svg class="card-edge" viewBox="0 0 1200 986" aria-hidden="true">
    <defs>
      <filter id="rough-edge" x="-5%" y="-5%" width="110%" height="110%">
        <feTurbulence type="fractalNoise" baseFrequency="0.09" numOctaves="2" seed="4"/>
        <feDisplacementMap in="SourceGraphic" scale="8"/>
      </filter>
    </defs>
    <rect x="232" y="249" width="733" height="445" fill="none"
          stroke="var(--edge-rose)" stroke-width="4" filter="url(#rough-edge)"/>
  </svg>

  <div class="foliage foliage--top" role="img" aria-label="Feine rosafarbene Zweige mit Blättern als Hintergrundornament"></div>
  <div class="foliage foliage--bottom" role="img" aria-label="Rosafarbener Blätterzweig als Hintergrundornament"></div>

  <h1 class="person-name">Kolu Trisvend</h1>
  <p class="contact">
    Mobil 079 634 18 27<br>
    kolu.trisvend@solvarin.ch
  </p>

  <div class="brand">
    <span class="brand__mark"></span>
    <span class="brand__name">Solvarin</span>
  </div>

  <p class="tagline">neues schaffen</p>

  <p class="address">
    <span class="address__web">www. solvarin.ch</span><br>
    <span class="address__street">Solvarin • Moosrain 12 &nbsp;• 8399 TALWIL</span>
  </p>
</main>
</body>
</html>
```